Discreet simple classy for adult entertainment

I would like a matte black business card with gold writing for my business. Keeping it simple. Having my following:

Lana frost
Events. Entertainment. Promotions
0491726580

or alternatively could have what i had on my previous card below but i think i prefer the above as again - discretion.

Maybe a nice gold line thru the card or some other very simple design . Or not open to ideas/ can be doublesided if any good ideas with that.

included pics of my old bus card. not sure weather i want a photo on it or not. if i do it wont be the same pic. i kinda wanted a card that was discreet so if it was in someones wallet they wouldn't neccessarily realise it was from a stripper.

Target Market(s)

men

Industry/Entity Type

Business

Contact Information for Business Card

Lana frost
0491726580

Requirements
Nice to have
• i don't know i am really open to anything. im giving my cards to guys so something they can have in their wallet that is discreet preferably.

```html
<!DOCTYPE html>
<html lang="en">
<head>
<meta charset="utf-8">
<title>Lana frost — business card</title>
<link rel="stylesheet" href="https://fonts.googleapis.com/css2?family=Marcellus&display=swap">
<style>
  :root {
    --card-black: #2a2928;
    --card-gold: #e8e232;
  }
  html, body {
    margin: 0;
    padding: 0;
    overflow: hidden;
    background: var(--card-black);
  }
  .card {
    position: relative;
    width: 1200px;
    height: 795px;
    background: var(--card-black);
    color: var(--card-gold);
    font-family: "Marcellus", serif;
    overflow: hidden;
  }
  .rule {
    position: absolute;
    height: 2px;
    background: var(--card-gold);
    top: 410px;
  }
  .rule--lead { left: 0; width: 103px; }
  .rule--main { left: 313px; width: 364px; }
  .heel-mark {
    position: absolute;
    left: 150px;
    top: 290px;
    width: 104px;
    height: 126px;
  }
  .name {
    position: absolute;
    right: 89px;
    top: 374px;
    margin: 0;
    font-size: 50px;
    font-weight: 400;
    line-height: 1;
    letter-spacing: 0.36em;
  }
  .phone {
    position: absolute;
    right: 90px;
    top: 466px;
    margin: 0;
    font-size: 32px;
    line-height: 1;
    letter-spacing: 0.3em;
  }
  .services {
    position: absolute;
    left: 0;
    right: 0;
    top: 664px;
    margin: 0;
    text-align: center;
    font-size: 40px;
    line-height: 1;
    letter-spacing: 0.26em;
  }
  .services__divider {
    display: inline-block;
    margin: 0 0.15em;
  }
</style>
</head>
<body>
  <main class="card">
    <div class="rule rule--lead"></div>
    <svg class="heel-mark" viewBox="0 0 104 126" role="img" aria-label="Small gold high-heel shoe emblem">
      <rect x="0" y="0" width="104" height="126" fill="var(--card-gold)"/>
    </svg>
    <div class="rule rule--main"></div>

    <h1 class="name">lana frost</h1>
    <p class="phone">0491726580</p>

    <p class="services">events<span class="services__divider">|</span>entertainment<span class="services__divider">|</span>promotions</p>
  </main>
</body>
</html>
```